First Aid Training business needs business card design

We would like a double sided business card designed for a first aid training business - Brindlewood First Aid. We provide first aid training and , WHS (work, health and safety) training.

The attached word document contains the key information we would like on each side of the business card.

Final design needs to be delivered in print ready format, along with the original file.

```html
<!DOCTYPE html>
<html lang="en">
<head>
<meta charset="utf-8">
<title>Brindlewood First Aid – Business Card</title>
<link rel="stylesheet" href="https://fonts.googleapis.com/css2?family=Montserrat:wght@600&family=Open+Sans:wght@400;700&display=swap">
<style>
  :root {
    --brand-red: #ec2227;
    --paper: #ffffff;
    --ink: #231f20;
    --page: #ffffff;
  }
  * { margin: 0; padding: 0; box-sizing: border-box; }
  html, body {
    width: 1200px; height: 900px; overflow: hidden;
    background: var(--page);
  }
  .card {
    position: absolute; left: 262px; width: 675px; height: 405px;
    background: var(--paper); overflow: hidden;
    font-family: "Open Sans", sans-serif;
  }
  .card--front { top: 28px; }
  .card--back { top: 467px; }
  .card__shape { position: absolute; inset: 0; width: 100%; height: 100%; }

  /* front */
  .brand-line {
    position: absolute; top: 66px; left: 0; right: 0;
    display: flex; justify-content: center; align-items: center; gap: 12px;
  }
  .brand-line__dot { width: 34px; height: 34px; border-radius: 50%; background: var(--brand-red); }
  .brand-line__name {
    font-family: "Montserrat", sans-serif; font-weight: 600;
    font-size: 22px; letter-spacing: 0.5px; color: var(--ink);
  }
  .headline {
    position: absolute; top: 208px; left: 0; right: 0; text-align: center;
    color: var(--paper); font-weight: 700; font-size: 22px; letter-spacing: 0.2px;
  }
  .benefits {
    position: absolute; top: 252px; left: 188px; width: 300px;
    list-style: none; display: flex; flex-direction: column; gap: 4px;
  }
  .benefits li {
    height: 21px; line-height: 21px; border-radius: 5px;
    background: var(--paper); color: var(--brand-red);
    text-align: center; font-size: 16px;
  }

  /* back */
  .brand-block {
    position: absolute; left: 40px; top: 95px; width: 270px;
    text-align: center; color: var(--paper);
    font-family: "Montserrat", sans-serif; font-weight: 600;
  }
  .brand-block__dot {
    width: 116px; height: 116px; border-radius: 50%;
    background: var(--paper); margin: 0 auto 24px;
  }
  .brand-block__name { font-size: 30px; line-height: 1.1; }
  .brand-block__sub { font-size: 20px; margin-top: 6px; }

  .holder {
    position: absolute; left: 355px; top: 112px;
    display: flex; align-items: center; gap: 14px;
  }
  .holder__name { font-weight: 700; font-size: 22px; color: var(--ink); }
  .contacts {
    position: absolute; left: 355px; top: 185px; list-style: none;
    display: flex; flex-direction: column; gap: 8px;
  }
  .contacts li { display: flex; align-items: center; gap: 12px; font-size: 16px; color: var(--ink); }
  .icon-tile {
    width: 29px; height: 31px; border-radius: 6px; background: var(--brand-red);
    display: flex; align-items: center; justify-content: center;
  }
</style>
</head>
<body>

<section class="card card--front">
  <svg class="card__shape" viewBox="0 0 1125 675" preserveAspectRatio="none" aria-hidden="true">
    <path d="M0 493 Q562 -21 1125 493 L1125 675 L0 675 Z" fill="var(--brand-red)"/>
  </svg>
  <div class="brand-line">
    <span class="brand-line__dot"></span>
    <span class="brand-line__name">BRINDLEWOOD FIRST AID</span>
  </div>
  <p class="headline">ONSITE TRAINING – WE CAN COME TO YOU</p>
  <ul class="benefits">
    <li>TIME EFFICIENT</li>
    <li>COST EFFECTIVE</li>
    <li>MINIMISE DOWNTIME FOR YOUR TEAM</li>
  </ul>
</section>

<section class="card card--back">
  <svg class="card__shape" viewBox="0 0 675 405" aria-hidden="true">
    <circle cx="105" cy="202" r="233" fill="var(--brand-red)"/>
  </svg>
  <div class="brand-block">
    <div class="brand-block__dot"></div>
    <div class="brand-block__name">BRINDLEWOOD</div>
    <div class="brand-block__sub">FIRST AID TRAINING</div>
  </div>

  <div class="holder">
    <svg width="28" height="34" viewBox="0 0 28 34" aria-hidden="true">
      <circle cx="14" cy="8" r="7.5" fill="var(--brand-red)"/>
      <path d="M0 34 V26 Q0 17 9 17 H19 Q28 17 28 26 V34 Z" fill="var(--brand-red)"/>
    </svg>
    <span class="holder__name">DALE PRITCHARD</span>
  </div>

  <ul class="contacts">
    <li>
      <span class="icon-tile">
        <svg width="17" height="17" viewBox="0 0 24 24" aria-hidden="true"><path fill="#fff" d="M6.6 10.8a15 15 0 0 0 6.6 6.6l2.2-2.2c.3-.3.7-.4 1-.2 1.1.4 2.3.6 3.6.6.6 0 1 .4 1 1V20c0 .6-.4 1-1 1A17 17 0 0 1 3 4c0-.6.4-1 1-1h3.5c.6 0 1 .4 1 1 0 1.3.2 2.5.6 3.6.1.3 0 .7-.2 1z"/></svg>
      </span>
      0412 555 038
    </li>
    <li>
      <span class="icon-tile">
        <svg width="16" height="12" viewBox="0 0 16 12" aria-hidden="true"><rect x="0.75" y="0.75" width="14.5" height="10.5" fill="none" stroke="#fff" stroke-width="1.3"/><path d="M1 1 L8 7 L15 1 M1 11 L6 6 M15 11 L10 6" fill="none" stroke="#fff" stroke-width="1.2"/></svg>
      </span>
      help@brindlewoodfirstaid.com.au
    </li>
    <li>
      <span class="icon-tile">
        <svg width="14" height="18" viewBox="0 0 14 18" aria-hidden="true"><path fill="#fff" d="M7 0a7 7 0 0 0-7 7c0 5 7 11 7 11s7-6 7-11a7 7 0 0 0-7-7zm0 10a3 3 0 1 1 0-6 3 3 0 0 1 0 6z"/></svg>
      </span>
      www.brindlewoodfirstaid.com.au
    </li>
  </ul>
</section>

</body>
</html>
```